nine-parts.com

We are a small dollar lending company that will revolutionize the industry. We will do this by being completely transparent, fee free, etc and an interest rate that normal people can afford to pay. Over 10X less than our competition. We only allow our members to pay bills " bills paid fast", within 72 hours. Payday loans typically charge from 390%-600% with a terrible payback structure. We charge 36%, period, with a payback structure over 12 months. Our site will be very simple and easy to use but elegant at the same time. We do not want the site to be too busy, less is more and easier. We will have; Home, The Story, Why 9parts.com, Are you eligible? Members, Clients. To become a member you have to be referred by a current client of 9parts.com. A lot of the busy stuff will be saved for the Members and Clients sections. The feel must be elegant, easy to use and very simple to understand. I am looking for the green, white and black combinations of colors, very similar to my logo that was designed by Pixelmoor.

```html
<!DOCTYPE html>
<html lang="en">
<head>
<meta charset="utf-8">
<title>Nine Parts – Dollar Lending</title>
<link href="https://fonts.googleapis.com/css2?family=Lato:wght@300;400;700&family=League+Gothic&display=swap" rel="stylesheet">
<style>
:root{
  --green:#8dc63f;
  --green-dark:#6fa82a;
  --green-hero:#8cc543;
  --ink:#222;
  --text:#3a3a3a;
  --bar:#2b2b2b;
  --bar-active:#000;
  --band:#eeeeee;
  --line:#dddddd;
  --social:#bdbdbd;
  --white:#fff;
}
*{box-sizing:border-box;margin:0;padding:0}
html,body{width:1120px;height:1200px;overflow:hidden;background:var(--white);font-family:"Lato",sans-serif;color:var(--text)}
.wrap{width:792px;margin:0 auto;position:relative}
a{color:inherit;text-decoration:none}

/* header */
.site-header{height:102px}
.site-header .wrap{height:102px}
.brand{position:absolute;left:8px;top:18px;display:flex;align-items:center;gap:10px}
.brand-dot{width:48px;height:48px;border-radius:50%;background:var(--green)}
.brand-name{font-size:30px;font-weight:400;color:var(--ink);letter-spacing:-.5px}
.social{position:absolute;right:0;top:26px;display:flex;gap:4px}
.social span{width:25px;height:25px;background:var(--social);display:block}
.call{position:absolute;right:0;top:60px;font-size:19px;font-weight:300;color:var(--green)}
.call strong{font-weight:400;color:var(--ink)}

/* nav */
.main-nav{background:var(--bar);height:39px}
.main-nav ul{list-style:none;display:flex;height:39px}
.main-nav li a{display:block;line-height:39px;padding:0 12px;color:var(--white);font-size:11.5px;text-transform:uppercase;letter-spacing:-.2px}
.main-nav li:first-child a{background:var(--bar-active);padding:0 18px}

/* hero */
.hero{background:var(--green-hero);height:312px}
.hero .wrap{height:312px}
.hero-art{position:absolute;left:0;top:0;width:420px;height:312px;background:linear-gradient(90deg,#1e9e45 0%,#2aad4e 45%,#5fbb47 80%,rgba(140,197,67,0) 100%)}
.hero-copy{position:absolute;left:399px;top:47px;width:356px}
.hero-title{font-family:"League Gothic",sans-serif;font-size:35px;font-weight:400;white-space:nowrap;color:var(--white);border-top:1px solid var(--white);border-bottom:1px solid var(--white);padding:6px 0 5px;line-height:45px;letter-spacing:0}
.perks{list-style:none;margin-top:14px}
.perks li{display:flex;align-items:center;gap:8px;color:var(--white);font-size:19.5px;font-weight:300;height:32px;white-space:nowrap}
.perks svg{width:20px;height:20px}

/* clients */
.clients{background:var(--band);height:113px;border-bottom:1px solid var(--line)}
.clients h2{position:absolute;left:6px;top:19px;font-size:16px;font-weight:400;color:var(--text)}
.client-row{position:absolute;left:10px;top:50px;width:780px;display:flex;justify-content:space-between;align-items:center}
.client{display:flex;align-items:center;gap:5px;font-size:12px;font-weight:700;color:#555}
.client i{width:9px;height:9px;background:var(--green);display:block;border-radius:50%}

/* content */
.content{height:378px}
.welcome{position:absolute;left:10px;top:40px;width:486px}
.welcome h1{font-size:37px;font-weight:400;color:var(--ink);margin-bottom:14px;letter-spacing:-.3px}
.welcome h1 span{color:var(--green)}
.welcome h3{font-size:12px;font-weight:700;color:var(--green);line-height:19px}
.welcome p{font-size:12px;line-height:19.2px;margin-bottom:19px}
.welcome p b{color:var(--ink)}
.welcome p u{color:var(--ink)}
.members{position:absolute;left:530px;top:52px;width:262px;height:308px;border:1px solid var(--line);padding:12px 14px}
.members h2{display:flex;align-items:center;gap:6px;font-size:19px;font-weight:400;color:var(--green);padding-bottom:8px;border-bottom:1px solid var(--line)}
.members p{font-size:12px;line-height:19.2px;padding:0 2px;margin-top:12px}
.members p+p{margin-top:19px}
.members .more{display:block;font-size:12px;font-weight:700;color:var(--green);margin:14px 0 0 4px}

/* eligibility banner */
.eligible{position:relative;margin:30px auto 0;width:781px;height:103px;background:var(--green);border-radius:2px;overflow:hidden;left:4px}
.eligible-art{position:absolute;left:0;top:0;width:220px;height:103px;background:linear-gradient(90deg,#6aae2e 0%,#7dbb38 65%,rgba(141,198,63,0) 100%)}
.eligible h2{position:absolute;left:216px;top:26px;font-size:40px;font-weight:300;color:var(--white);letter-spacing:.3px}
.discover{position:absolute;right:26px;top:27px;width:136px;height:48px;background:#a5d960;border:1px solid #c2e68f;border-radius:3px;box-shadow:0 3px 0 #6e9f33;font-size:12px;font-weight:700;text-transform:uppercase;color:#3a4a22;display:flex;align-items:center;justify-content:center}

/* footer */
.site-footer{position:absolute;left:0;top:1128px;width:1120px;height:72px;background:var(--bar);text-align:center;color:var(--white)}
.footer-nav{margin-top:20px;font-size:11.5px;text-transform:uppercase}
.footer-nav span{color:#999;margin:0 4px}
.copyright{font-size:11px;color:#bbb;margin-top:7px}
</style>
</head>
<body>
<header class="site-header">
  <div class="wrap">
    <a class="brand" href="#"><span class="brand-dot"></span><span class="brand-name">NINE PARTS</span></a>
    <div class="social"><span></span><span></span><span></span><span></span></div>
    <div class="call">CALL US <strong>555.014.2290</strong></div>
  </div>
</header>

<nav class="main-nav">
  <div class="wrap">
    <ul>
      <li><a href="#">Home</a></li>
      <li><a href="#">The Story</a></li>
      <li><a href="#">Why 9parts.com</a></li>
      <li><a href="#">Are you eligible?</a></li>
      <li><a href="#">Members</a></li>
      <li><a href="#">Clients</a></li>
      <li><a href="#">Contact Us</a></li>
    </ul>
  </div>
</nav>

<section class="hero">
  <div class="wrap">
    <div class="hero-art" role="img" aria-label="Row of large green 3D dollar signs receding into the distance"></div>
    <div class="hero-copy">
      <h2 class="hero-title">WE ARE A DOLLAR LENDING COMPANY</h2>
      <ul class="perks">
        <li><svg viewBox="0 0 20 20"><polyline points="2,11 7,16 18,4" fill="none" stroke="#fff" stroke-width="3"/></svg>Completely Transparent</li>
        <li><svg viewBox="0 0 20 20"><polyline points="2,11 7,16 18,4" fill="none" stroke="#fff" stroke-width="3"/></svg>Fee Free Service</li>
        <li><svg viewBox="0 0 20 20"><polyline points="2,11 7,16 18,4" fill="none" stroke="#fff" stroke-width="3"/></svg>Affordable Interest Rate</li>
        <li><svg viewBox="0 0 20 20"><polyline points="2,11 7,16 18,4" fill="none" stroke="#fff" stroke-width="3"/></svg>Pay Bills within 72 hours and</li>
        <li><svg viewBox="0 0 20 20"><polyline points="2,11 7,16 18,4" fill="none" stroke="#fff" stroke-width="3"/></svg>Much more</li>
      </ul>
    </div>
  </div>
</section>

<section class="clients">
  <div class="wrap">
    <h2>Our Clients</h2>
    <div class="client-row">
      <span class="client"><i></i>Velora</span>
      <span class="client"><i></i>Dunmark</span>
      <span class="client"><i></i>Crestwhip</span>
      <span class="client"><i></i>Wavecraft</span>
      <span class="client"><i></i>Ironloop</span>
      <span class="client"><i></i>Harvest Table</span>
      <span class="client"><i></i>Kernel &amp; Co</span>
    </div>
  </div>
</section>

<main class="content">
  <div class="wrap">
    <article class="welcome">
      <h1>Welcome to <span>Nine</span> Parts</h1>
      <h3>Lorem ipsum dolor sit amet, consectetur adipiscing elit.</h3>
      <p>Sed quis nisi euismod, fermentum tellus a, lobortis quam. Vestibulum condimentum mi vitae diam tristique, egestas dignissim diam mattis. <b>Curabitur vel diam</b> in massa porttitor dictum id in lorem. Vivamus faucibus ac leo ac dignissim.</p>
      <p>Maecenas orci est, euismod facilisis feugiat sit amet, semper ut tortor. Donec eleifend accumsan nisl, nec laoreet leo iaculis sit amet. Vivamus eu <u>magna rhoncus</u>, consectetur metus ac, varius lacus. Donec ultricies, tortor quis sagittis sagittis, mauris erat ullamcorper augue, eu placerat diam nunc a lorem.</p>
      <h3>Nam vulputate mauris id arcu pharetra</h3>
      <p>Nullam eget massa vel mi posuere venenatis sed quis tortor. In hac habitasse platea dictumst. Fusce nisi tellus, fermentum a luctus eget, convallis vitae orci. In commodo egestas magna quis placerat.</p>
    </article>
    <aside class="members">
      <h2><svg width="28" height="20" viewBox="0 0 28 20"><circle cx="9" cy="6" r="5" fill="#b5b5b5"/><path d="M0 20c0-6 4-8 9-8s9 2 9 8z" fill="#b5b5b5"/><circle cx="19" cy="5" r="4.5" fill="#b5b5b5"/><path d="M14 11c2-1 4-1.5 5-1.5 5 0 9 2 9 8h-9c0-3-2-5-5-6.5z" fill="#b5b5b5"/></svg>MEMBERS</h2>
      <p>Aenean posuere velit a erat placerat, id euismod magna rutrum. Curabitur ac sollicitudin tellus. Aenean gravida nisl ut ligula facilisis, sed sollicitudin ipsum hendrerit.</p>
      <p>Vestibulum lacinia congue commodo. Sed lorem erat, euismod at risus at, sollicitudin venenatis risus. Praesent cursus lacus ac eros feugiat, vitae eleifend felis hendrerit.</p>
      <a class="more" href="#">Know More&gt;</a>
    </aside>
  </div>
</main>

<section class="eligible">
  <div class="eligible-art" role="img" aria-label="Pale green graphic of raised hands giving thumbs up with swirl circles"></div>
  <h2>ARE YOU ELIGIBLE?</h2>
  <a class="discover" href="#">Discover Now</a>
</section>

<footer class="site-footer">
  <div class="footer-nav">Home<span>/</span>The Story<span>/</span>Why 9parts.com<span>/</span>Are you eligible?<span>/</span>Members<span>/</span>Clients<span>/</span>Contact Us</div>
  <div class="copyright">Copyright © 2014 nine-parts.com. All rights reserved.</div>
</footer>
</body>
</html>
```